Brivane - Business Cards for a new venture

create business card for a startup classified business dealing in construction materials, the cards need to have a professional look but modern, more serious than playful, one of the samples must include the official font (attached), please explore using the official colors in the company's logo

Target Market(s)

Energy sector

Contact Information for Business Card

Font styles to use
Other font styles liked:
• suissnord

Requirements
Must have
• corporate colors (in logo attached)
Nice to have
• Official font (in one of the samples) font is : suissnord
Should not have
• Cartoonish look

```html
<!DOCTYPE html>
<html lang="en">
<head>
<meta charset="utf-8">
<title>Brivane – Business Cards</title>
<link rel="stylesheet" href="https://fonts.googleapis.com/css2?family=Syncopate:wght@400;700&display=swap">
<style>
  :root {
    --navy: #134475;
    --grey: #8f9094;
    --white: #ffffff;
    --backdrop: #e9e4de;
    --edge: #5a5a5a;
    --brand-font: "Syncopate", sans-serif;
  }
  * { margin: 0; padding: 0; box-sizing: border-box; }
  html, body { width: 1200px; height: 1200px; overflow: hidden; }
  body { background: var(--backdrop); position: relative; font-family: var(--brand-font); }

  .card {
    position: absolute;
    width: 840px;
    height: 480px;
    background: var(--white);
    border: 1px solid var(--edge);
    overflow: hidden;
    box-shadow: 0 6px 14px rgba(0,0,0,0.25);
  }

  /* Front */
  .card--front { left: 42px; top: 86px; border-radius: 32px; }
  .brand {
    position: absolute;
    left: 0; right: 0; top: 210px;
    display: flex; align-items: center; justify-content: center; gap: 18px;
  }
  .brand__mark { width: 22px; height: 22px; background: var(--navy); }
  .brand__name {
    color: var(--grey);
    font-size: 38px;
    font-weight: 400;
    letter-spacing: 4px;
    text-transform: uppercase;
  }

  /* Back */
  .card--back { left: 298px; top: 650px; border-radius: 32px 0 32px 0; }
  .card__band { position: absolute; inset: 0; width: 100%; height: 100%; }

  .person { position: absolute; top: 96px; left: 108px; width: 240px; text-align: center; color: var(--navy); }
  .person__name { font-size: 24px; font-weight: 700; letter-spacing: 1px; line-height: 1.2; }
  .person__role { font-size: 16px; letter-spacing: 1px; margin-top: 6px; text-transform: uppercase; }

  .contact { position: absolute; display: flex; align-items: center; gap: 14px; color: var(--white); font-size: 15px; letter-spacing: 1px; white-space: nowrap; }
  .contact svg { width: 24px; height: 24px; flex: none; }
  .contact--mobile { left: 354px; top: 322px; }
  .contact--phone  { left: 324px; top: 357px; }
  .contact--email  { left: 294px; top: 391px; }
  .contact--addr   { left: 262px; top: 426px; text-transform: uppercase; }
</style>
</head>
<body>

<section class="card card--front">
  <div class="brand">
    <span class="brand__mark"></span>
    <span class="brand__name">Brivane</span>
  </div>
</section>

<section class="card card--back">
  <svg class="card__band" viewBox="0 0 840 480" preserveAspectRatio="none" aria-hidden="true">
    <polygon points="728,0 840,0 840,480 162,480" fill="var(--navy)"/>
  </svg>

  <div class="person">
    <div class="person__name">Name</div>
    <div class="person__role">Designation</div>
  </div>

  <div class="contact contact--mobile">
    <svg viewBox="0 0 24 24" fill="none" stroke="#fff" stroke-width="1.5"><circle cx="12" cy="12" r="11"/><rect x="8.5" y="6" width="7" height="12" rx="1.2"/><line x1="11" y1="15.5" x2="13" y2="15.5"/></svg>
    <span>0147 258369</span>
  </div>
  <div class="contact contact--phone">
    <svg viewBox="0 0 24 24" fill="none" stroke="#fff" stroke-width="1.5"><circle cx="12" cy="12" r="11"/><path d="M8 7.5c0 5 3.5 8.5 8.5 8.5l1-2-2.5-1.2-1.2 1.2c-1.6-.7-2.7-1.8-3.3-3.3l1.2-1.2L10.5 7 8 7.5z" fill="#fff"/></svg>
    <span>994 83726150</span>
  </div>
  <div class="contact contact--email">
    <svg viewBox="0 0 24 24" fill="none" stroke="#fff" stroke-width="1.5"><circle cx="12" cy="12" r="11"/><rect x="6.5" y="8" width="11" height="8" fill="#fff"/><path d="M6.5 8l5.5 4.5L17.5 8" stroke="var(--navy)"/></svg>
    <span>@brivane.com</span>
  </div>
  <div class="contact contact--addr">
    <svg viewBox="0 0 24 24" fill="none" stroke="#fff" stroke-width="1.5"><circle cx="12" cy="12" r="11"/><path d="M12 18.5s-4.5-4.6-4.5-8a4.5 4.5 0 0 1 9 0c0 3.4-4.5 8-4.5 8z"/><circle cx="12" cy="10.5" r="1.6"/></svg>
    <span>Address</span>
  </div>
</section>

</body>
</html>
```